Journeys With Marcella Business Cards

I need a business card design for my upscale Travel Agency.
Attached you can find my logo.
I would like to include the following:
- Name
- Title
- Phone Number
- Email
- Website
- and then something like: Follow us: JourneysWithMarcella (and then social media icons in color).
The logo should be in the front and then also the back.
I am also attaching a design that I liked (mostly for the layout) but open to any suggestions
Industry/Entity Type
Travel Agent
Contact Information for Business Card
Name: Marcella Dorn
Title: Travel Designer / Owner
Phone: 415-927-3308
Email: marcella@journeyswithmarcella-example.com
Website: www.JourneysWithMarcella-example.com
Social Media Handles for FB,IG, Twitter: JourneysWithMarcella
Colors
Designer to choose colors to be used in the design.
Look and feel

```html
<!DOCTYPE html>
<html lang="en">
<head>
<meta charset="utf-8">
<title>Journeys With Marcella – Business Cards</title>
<link rel="stylesheet" href="https://fonts.googleapis.com/css2?family=Lato:wght@400;700&display=swap">
<style>
  :root {
    --backdrop: #2a2a2b;
    --card-top: #141414;
    --card-bottom: #070707;
    --accent: #f4a24e;
    --text-light: #e9e9e9;
    --text-muted: #bdbdbd;
    --divider: #5a5a5a;
  }
  * { box-sizing: border-box; margin: 0; padding: 0; }
  html, body {
    width: 1200px; height: 900px; overflow: hidden;
    background: var(--backdrop);
    font-family: "Lato", Arial, sans-serif;
  }
  .canvas { position: relative; width: 1200px; height: 900px; }

  .card {
    position: absolute; left: 250px; width: 700px; height: 380px;
    background: linear-gradient(160deg, var(--card-top), var(--card-bottom));
    overflow: hidden;
  }
  .card--front { top: 55px; }
  .card--back { top: 465px; }
  .card__stripe {
    position: absolute; left: 0; right: 0; bottom: 0; height: 10px;
    background: var(--accent);
  }

  .brand {
    position: absolute; display: flex; align-items: center; gap: 14px;
    color: var(--accent); font-weight: 700; font-size: 30px; letter-spacing: 0.5px;
    white-space: nowrap;
  }
  .brand__mark { width: 18px; height: 18px; background: var(--accent); flex: none; }
  .card--front .brand { left: 50%; top: 130px; transform: translateX(-50%); }
  .card--back .brand { right: 70px; top: 70px; }

  .social {
    position: absolute; left: 50%; top: 235px; transform: translateX(-50%);
    display: flex; align-items: center; gap: 10px;
    color: var(--text-light); font-size: 18px;
  }
  .social__dot { width: 14px; height: 14px; border-radius: 50%; background: var(--accent); }

  .identity {
    position: absolute; left: 40px; top: 185px; width: 270px; text-align: right;
  }
  .identity__name {
    color: var(--accent); font-weight: 700; font-size: 22px; text-transform: uppercase;
    letter-spacing: 0.3px;
  }
  .identity__title { color: var(--text-muted); font-size: 17px; margin-top: 4px; }

  .divider {
    position: absolute; left: 330px; top: 180px; width: 1px; height: 110px;
    background: var(--divider);
  }

  .contact {
    position: absolute; left: 352px; top: 188px; list-style: none;
    color: var(--text-light); font-size: 15px;
  }
  .contact__item { display: flex; align-items: center; gap: 9px; height: 30px; white-space: nowrap; }
  .contact__icon { width: 14px; height: 14px; flex: none; fill: var(--accent); }
</style>
</head>
<body>
<main class="canvas">

  <section class="card card--front" aria-label="Business card front">
    <div class="brand"><span class="brand__mark"></span>Journeys With Marcella</div>
    <div class="social"><span class="social__dot"></span>JourneysWithMarcella</div>
    <div class="card__stripe"></div>
  </section>

  <section class="card card--back" aria-label="Business card back">
    <div class="brand"><span class="brand__mark"></span>Journeys With Marcella</div>

    <div class="identity">
      <p class="identity__name">Marcella Dorn</p>
      <p class="identity__title">Travel Designer / Owner</p>
    </div>

    <div class="divider"></div>

    <ul class="contact">
      <li class="contact__item">
        <svg class="contact__icon" viewBox="0 0 16 16" aria-hidden="true"><path d="M3.6 1.5l2.3 2.6-1.3 1.9c.9 2 2.5 3.6 4.5 4.5l1.9-1.3 2.6 2.3-1.4 2.4C7 13.6 2.4 9 1.2 3z"/></svg>
        415-927-3308
      </li>
      <li class="contact__item">
        <svg class="contact__icon" viewBox="0 0 16 16" aria-hidden="true"><path d="M1 3h14v10H1z M2 4.2v.4l6 4 6-4v-.4z" fill-rule="evenodd"/></svg>
        marcella@journeyswithmarcella-example.com
      </li>
      <li class="contact__item">
        <svg class="contact__icon" viewBox="0 0 16 16" aria-hidden="true"><circle cx="8" cy="8" r="7"/><path d="M1 8h14M8 1c-3 3.5-3 10.5 0 14M8 1c3 3.5 3 10.5 0 14" stroke="#0c0c0c" stroke-width="1.1" fill="none"/></svg>
        www.JourneysWithMarcella-example.com
      </li>
    </ul>

    <div class="card__stripe"></div>
  </section>

</main>
</body>
</html>
```